Derek Milbourne needs a single album cover

I need an single album cover for a song I wrote called "Still Harbor". I would like the design to Illustrate how gods grace covers all sin.

Requirements
Must have
• The song title "Still Harbor" And my name Derek Milbourne

```html
<!DOCTYPE html>
<html lang="en">
<head>
<meta charset="utf-8">
<title>Derek Milbourne – Still Harbor</title>
<link rel="stylesheet" href="https://fonts.googleapis.com/css2?family=Comfortaa:wght@400;700&family=Quicksand:wght@400;500;700&display=swap">
<style>
  :root {
    --frame: #000000;
    --paper: #daf4ef;
    --ink: #0a0a0a;
    --ash: #8fa6a0;
    --mist: #a9e6d6;
    --sea: #72d8b6;
    --mint: #55d39e;
    --leaf: #36bd7a;
    --deep: #1f5e4c;
    --neon: #19e65a;
    --white: #ffffff;
  }
  html, body {
    margin: 0;
    padding: 0;
    width: 1200px;
    height: 1160px;
    overflow: hidden;
    background: var(--white);
  }
  .cover {
    position: relative;
    width: 1200px;
    height: 1160px;
    background: var(--frame);
  }
  .cover__field {
    position: absolute;
    left: 27px;
    top: 24px;
    width: 1146px;
    height: 1112px;
    background: var(--paper);
    box-shadow: inset 0 0 40px 14px rgba(0, 0, 0, 0.85);
  }
  .cover__art {
    position: absolute;
    left: 0;
    top: 0;
    width: 1200px;
    height: 1160px;
  }
  .word { font-family: "Quicksand", sans-serif; font-weight: 500; }
  .word--bold { font-weight: 700; }
  .artist {
    font-family: "Comfortaa", sans-serif;
    font-weight: 700;
    fill: var(--white);
    stroke: var(--ink);
    stroke-width: 9px;
    paint-order: stroke;
    letter-spacing: 2px;
  }
  .title-lead { font-family: "Quicksand", sans-serif; font-weight: 500; fill: var(--ink); }
  .title {
    font-family: "Comfortaa", sans-serif;
    font-weight: 700;
    fill: var(--ink);
    stroke: var(--neon);
    stroke-width: 14px;
    paint-order: stroke;
  }
  .c-ink { fill: var(--ink); }
  .c-ash { fill: var(--ash); }
  .c-mist { fill: var(--mist); }
  .c-sea { fill: var(--sea); }
  .c-mint { fill: var(--mint); }
  .c-leaf { fill: var(--leaf); }
  .c-deep { fill: var(--deep); }
</style>
</head>
<body>
<div class="cover">
  <div class="cover__field"></div>
  <svg class="cover__art" viewBox="0 0 1200 1160" xmlns="http://www.w3.org/2000/svg">
    <text class="artist" x="600" y="153" font-size="78" text-anchor="middle" textLength="780" lengthAdjust="spacingAndGlyphs">DEREK MILBOURNE</text>

    <g class="words words--storm">
      <text class="word c-mist" x="300" y="270" font-size="50">doubt.</text>
      <text class="word c-mist" x="490" y="270" font-size="30">envy.</text>
      <text class="word c-mist" x="600" y="270" font-size="32">bitterness.</text>
      <text class="word c-sea" x="800" y="270" font-size="34">deceit.</text>

      <text class="word c-ash" x="170" y="345" font-size="80" textLength="300" lengthAdjust="spacingAndGlyphs">SHAME.</text>
      <text class="word c-sea" x="495" y="345" font-size="36">greed.</text>
      <text class="word c-mist" x="625" y="345" font-size="32">restless.</text>
      <text class="word c-mist" x="790" y="345" font-size="40">anger.</text>

      <text class="word c-mist" x="330" y="410" font-size="46">guilt.</text>
      <text class="word c-mist" x="480" y="410" font-size="48">wandering.</text>
      <text class="word c-mist" x="745" y="410" font-size="44">regret.</text>

      <text class="word c-sea" x="380" y="500" font-size="90" textLength="450" lengthAdjust="spacingAndGlyphs">despair.</text>
      <text class="word c-mist" x="860" y="455" font-size="22">storm and</text>
      <text class="word c-mist" x="858" y="500" font-size="44">sorrow.</text>
    </g>

    <text class="title-lead" x="127" y="545" font-size="96">still</text>
    <text class="title" x="130" y="745" font-size="220" textLength="850" lengthAdjust="spacingAndGlyphs">harbor.</text>

    <g class="words words--calm">
      <text class="word c-leaf" x="300" y="820" font-size="60">mercy.</text>
      <text class="word c-leaf" x="525" y="820" font-size="30">kindness.</text>
      <text class="word c-mint" x="690" y="820" font-size="32">patience.</text>

      <text class="word c-ink" x="160" y="895" font-size="66" textLength="230" lengthAdjust="spacingAndGlyphs">PEACE.</text>
      <text class="word c-mint" x="420" y="895" font-size="34">forgiven.</text>
      <text class="word c-deep" x="600" y="895" font-size="36">anchored.</text>
      <text class="word word--bold c-ink" x="795" y="895" font-size="32">renewed.</text>

      <text class="word c-leaf" x="390" y="960" font-size="48">grateful.</text>
      <text class="word word--bold c-leaf" x="615" y="960" font-size="48">steadfast.</text>
      <text class="word word--bold c-deep" x="860" y="960" font-size="50">rest.</text>

      <text class="word c-leaf" x="380" y="1060" font-size="104" textLength="540" lengthAdjust="spacingAndGlyphs">redeemed.</text>
      <text class="word word--bold c-deep" x="945" y="1020" font-size="24">safe</text>
      <text class="word word--bold c-deep" x="942" y="1060" font-size="44">shore.</text>
    </g>
  </svg>
</div>
</body>
</html>
```